Property Management Company looking for a high-end business card, letterhead and envelope design.

We provide high-end / boutique property management for real estate investors or individuals looking for someone to manage their portfolio. we are looking for a cohesive high-end design for our business cards, letterhead and envelopes.

Target Market(s)

Real Estate Investors

Industry/Entity Type

Real Estate

Requirements
Must have
• business card, letterhead and envelope design - logo attached

```html
<!DOCTYPE html>
<html lang="en">
<head>
<meta charset="utf-8">
<title>Northvale Stationery Set</title>
<link rel="stylesheet" href="https://fonts.googleapis.com/css2?family=Poppins:wght@400;500;600&family=Lato:wght@400;700&display=swap">
<style>
  :root {
    --navy: #0b4a85;
    --grey: #a3a5a8;
    --paper: #ffffff;
    --backdrop: #ececec;
    --ink: #2b2b2b;
    --window: #e6e7e9;
  }
  * { margin: 0; padding: 0; box-sizing: border-box; }
  html, body { width: 866px; height: 1200px; overflow: hidden; background: var(--backdrop); }
  body { position: relative; font-family: "Lato", sans-serif; color: var(--ink); }

  .sheet { position: absolute; background: var(--paper); overflow: hidden; }

  /* plain footer band: thin grey rule above a straight navy bar */
  .footer-band { position: absolute; left: 0; right: 0; bottom: 0; height: var(--band, 10px); background: var(--navy); }
  .footer-band::before {
    content: ""; position: absolute; left: 0; right: 0; top: calc(var(--rule-gap, 4px) * -1 - 2px);
    height: 2px; background: var(--grey);
  }
  .card-front .footer-band { --band: 5px; --rule-gap: 2px; }
  .letterhead .footer-band, .envelope-front .footer-band { --band: 10px; --rule-gap: 4px; }

  .brand-name {
    font-family: "Poppins", sans-serif; font-weight: 600; color: var(--navy);
    letter-spacing: 0.14em; line-height: 1; white-space: nowrap;
  }

  /* business cards */
  .card-front { left: 82px; top: 81px; width: 149px; height: 84px; border-radius: 4px; }
  .card-front .brand-name { position: absolute; left: 9px; top: 36px; font-size: 8px; }
  .card-front .divider { position: absolute; left: 82px; top: 18px; width: 0.6px; height: 46px; background: var(--grey); }
  .card-front .holder { position: absolute; left: 87px; top: 19px; font-family: "Poppins", sans-serif; white-space: nowrap; }
  .holder-name { font-size: 5.4px; font-weight: 600; color: var(--navy); letter-spacing: 0.04em; }
  .holder-role { font-size: 3.4px; margin-top: 1px; }
  .holder-address { font-size: 3.4px; line-height: 4.4px; margin-top: 2px; }
  .holder-contact { font-size: 3.4px; line-height: 4.4px; margin-top: 1px; list-style: none; }
  .holder-contact li { display: flex; align-items: center; gap: 2px; }
  .holder-contact li.web { color: var(--navy); }
  .holder-contact svg { width: 3px; height: 3px; flex: none; }

  .card-back { left: 256px; top: 81px; width: 150px; height: 84px; border-radius: 4px; background: var(--navy); }
  .card-back .brand-name { position: absolute; left: 0; right: 0; top: 36px; text-align: center; font-size: 10px; color: var(--paper); }
  .card-back .web { position: absolute; left: 0; right: 0; bottom: 7px; text-align: center; font-size: 3.6px; color: var(--paper); letter-spacing: 0.06em; }

  /* letterheads */
  .letterhead { top: 207px; height: 433px; }
  .letterhead-blank { left: 88px; width: 306px; }
  .letterhead-word { left: 455px; width: 334px; }
  .letterhead .brand-name { position: absolute; top: 40px; font-size: 15px; }
  .letterhead-blank .brand-name { left: 19px; }
  .letterhead-word .brand-name { left: 21px; }

  .contact-block {
    position: absolute; top: 25px; padding-left: 6px; border-left: 0.7px solid var(--grey);
    font-family: "Poppins", sans-serif; font-size: 6.2px; line-height: 8.2px; list-style: none;
    white-space: nowrap;
  }
  .letterhead-blank .contact-block { right: 18px; }
  .letterhead-word .contact-block { right: 18px; }
  .contact-block li { display: flex; align-items: center; gap: 3px; }
  .contact-block li.gap { margin-top: 3px; }
  .contact-block svg { width: 5px; height: 5px; flex: none; }

  .letter { position: absolute; left: 21px; top: 130px; width: 292px; font-size: 5px; line-height: 8.4px; }
  .recipient-name { color: var(--navy); font-size: 6px; }
  .recipient { margin-bottom: 10px; }
  .letter p { margin-bottom: 8.5px; text-align: justify; }
  .signature { display: block; width: 40px; height: 12px; margin-top: 2px; border-radius: 2px; background: linear-gradient(90deg, #d9dde3, #eef0f3); }

  .label {
    position: absolute; font-family: "Lato", sans-serif; color: var(--navy); font-size: 16px;
    text-align: center; transform: translateX(-50%); white-space: nowrap;
  }
  .label-letterhead { left: 223px; top: 665px; }
  .label-word { left: 643px; top: 665px; }
  .label-envelope { left: 433px; top: 1098px; font-size: 30px; }

  /* envelopes */
  .envelope-back { top: 732px; width: 349px; height: 156px; }
  .envelope-back.flat-flap { left: 74px; }
  .envelope-back.curved-flap { left: 443px; }
  .envelope-back .flap { position: absolute; left: 0; top: 0; width: 100%; height: 100%; }
  .envelope-back .web {
    position: absolute; left: 0; right: 0; bottom: 17px; text-align: center;
    font-family: "Poppins", sans-serif; font-size: 7.8px; letter-spacing: 0.2em; color: var(--ink);
  }

  .envelope-front { top: 903px; height: 152px; }
  .envelope-front.plain { left: 74px; width: 341px; }
  .envelope-front.windowed { left: 443px; width: 342px; }
  .envelope-front .brand-name { position: absolute; left: 23px; top: 24px; font-size: 14px; }
  .return-address {
    position: absolute; left: 23px; top: 51px; font-family: "Poppins", sans-serif;
    font-size: 8px; line-height: 11px; padding-top: 2px; border-top: 0.7px solid var(--grey);
    white-space: nowrap;
  }
  .address-window { position: absolute; left: 211px; top: 72px; width: 114px; height: 57px; border-radius: 7px; background: var(--window); }
</style>
</head>
<body>

<svg width="0" height="0" style="position:absolute" aria-hidden="true">
  <defs>
    <symbol id="icon-phone" viewBox="0 0 10 10">
      <path d="M2 1 L4 1 L4.6 3.2 L3.4 4 C4 5.4 4.8 6.2 6 6.7 L6.8 5.5 L9 6.1 L9 8.2 C5 8.6 1.4 5 1.8 1 Z" fill="#0b4a85"/>
    </symbol>
    <symbol id="icon-mail" viewBox="0 0 10 10">
      <rect x="1" y="2.2" width="8" height="5.6" fill="none" stroke="#0b4a85" stroke-width="1"/>
      <path d="M1 2.4 L5 5.5 L9 2.4" fill="none" stroke="#0b4a85" stroke-width="1"/>
    </symbol>
    <symbol id="icon-web" viewBox="0 0 10 10">
      <circle cx="5" cy="5" r="4" fill="#0b4a85"/>
      <path d="M1 5 H9 M5 1 C3 3 3 7 5 9 M5 1 C7 3 7 7 5 9" stroke="#fff" stroke-width="0.6" fill="none"/>
    </symbol>
  </defs>
</svg>

<!-- Business cards -->
<section class="sheet card-front" aria-label="Business card, front">
  <div class="brand-name">NORTHVALE</div>
  <div class="divider"></div>
  <div class="holder">
    <div class="holder-name">CLARA VENHOLT</div>
    <div class="holder-role">President</div>
    <div class="holder-address">4410 Harbor Lane #210<br>Lakemont, FL 33610</div>
    <ul class="holder-contact">
      <li><svg><use href="#icon-phone"/></svg>+31 (0)20 555 01 42</li>
      <li><svg><use href="#icon-mail"/></svg>info@northvale-pm.com</li>
      <li class="web"><svg><use href="#icon-web"/></svg>www.northvale-pm.com</li>
    </ul>
  </div>
  <div class="footer-band"></div>
</section>

<section class="sheet card-back" aria-label="Business card, back">
  <div class="brand-name">NORTHVALE</div>
  <div class="web">www.northvale-pm.com</div>
</section>

<!-- Letterheads -->
<section class="sheet letterhead letterhead-blank" aria-label="Letterhead">
  <div class="brand-name">NORTHVALE</div>
  <ul class="contact-block">
    <li>4410 Harbor Lane</li>
    <li>#210 Lakemont, FL 33610</li>
    <li class="gap"><svg><use href="#icon-phone"/></svg>+31 (0)20 555 01 42</li>
    <li><svg><use href="#icon-mail"/></svg>info@northvale-pm.com</li>
    <li><svg><use href="#icon-web"/></svg>www.northvale-pm.com</li>
  </ul>
  <div class="footer-band"></div>
</section>

<section class="sheet letterhead letterhead-word" aria-label="Word document letterhead">
  <div class="brand-name">NORTHVALE</div>
  <ul class="contact-block">
    <li>4410 Harbor Lane</li>
    <li>#210 Lakemont, FL 33610</li>
    <li class="gap"><svg><use href="#icon-phone"/></svg>+31 (0)20 555 01 42</li>
    <li><svg><use href="#icon-mail"/></svg>info@northvale-pm.com</li>
    <li><svg><use href="#icon-web"/></svg>www.northvale-pm.com</li>
  </ul>
  <div class="letter">
    <div class="recipient">
      <div class="recipient-name">Dear, Peter L. Ormsby</div>
      <div>President</div>
      <div>Suite 204</div>
      <div>1270 Meadow Ave</div>
      <div>Riverton, MO 63150 USA</div>
    </div>
    <p>We are pleased to confirm that your property portfolio review has been completed. Our team has examined each unit, the current leases and the upcoming maintenance plans. Please find our summary of findings attached, along with recommendations for rent adjustments, tenant retention and scheduled repairs across all managed buildings this coming quarter. We look forward to discussing the next steps with you.</p>
    <p>Our monthly reports will continue to arrive on the first business day of each month. They include occupancy rates, collected rent, outstanding balances and all completed work orders, so you always have a clear view of how each of your investments is performing.</p>
    <p>Should you have any questions about this letter or the attached documents, please contact our office at any time. We value your trust and remain committed to careful, attentive management of your properties.</p>
    <div>Sincerely</div>
    <span class="signature" role="img" aria-label="Handwritten signature of Clara Venholt"></span>
  </div>
  <div class="footer-band"></div>
</section>

<div class="label label-letterhead">Letterhead</div>
<div class="label label-word">Word Document Letterhead</div>

<!-- Envelopes -->
<section class="sheet envelope-back flat-flap" aria-label="Envelope back, straight flap">
  <svg class="flap" viewBox="0 0 349 156" preserveAspectRatio="none">
    <path d="M0,0 H349 L345,58 H4 Z" fill="#0b4a85"/>
  </svg>
  <div class="web">www.northvale-pm.com</div>
</section>

<section class="sheet envelope-back curved-flap" aria-label="Envelope back, pointed flap">
  <svg class="flap" viewBox="0 0 349 156" preserveAspectRatio="none">
    <path d="M0,0 H349 L347,30 C346,42 338,47 326,48 L188,62 C180,63 169,63 161,62 L22,48 C10,47 3,42 2,30 Z" fill="#0b4a85"/>
  </svg>
  <div class="web">www.northvale-pm.com</div>
</section>

<section class="sheet envelope-front plain" aria-label="Envelope front">
  <div class="brand-name">NORTHVALE</div>
  <div class="return-address">4410 Harbor Lane #210<br>Lakemont, FL 33610</div>
  <div class="footer-band"></div>
</section>

<section class="sheet envelope-front windowed" aria-label="Window envelope front">
  <div class="brand-name">NORTHVALE</div>
  <div class="return-address">4410 Harbor Lane #210<br>Lakemont, FL 33610</div>
  <div class="address-window"></div>
  <div class="footer-band"></div>
</section>

<div class="label label-envelope">Envelope design</div>

</body>
</html>
```